Mental Health Non-profit Website that takes donations

We are a faith friendly non profit mental health agency. We need an about us section, a section for taking donations, and a place to list all our therapists and a photo of them
Unfortunately, many of our neighbors in Ohio face mental health challenges which harm their quality of life. Thousands of Ohioans experience trauma, addiction, anxiety, and depression, and the negative outcomes of these experiences continue to grow. While we know that data-driven counseling can improve quality of life for those with mental health challenges, many face economic and social barriers to accessing this transformational care.
Lanterns of Calm crosses barriers to mental health care for Ohioans. We are a nonprofit team of counselors dedicated to employing best practices in modes accessible to people of all backgrounds. A trauma-informed, faith-sensitive methodology uniquely equips us to address holistic mental health challenges. Donor support and community partnerships allow us to meet and serve individuals who could not otherwise access professional care.

Target Market(s)

Those seeking mental health therapy

Industry/Entity Type

Mental Health Non-profit

Coding

Coded - Design and coding required

Colors

Designer to choose colors to be used in the design.

Requirements
Must have
• Our logo colors of navy blue and gold, our logo, about us section, our mission section, a place to accept donations page for all of our therapists and their pictures, and a place for blog posts

```html
<!DOCTYPE html>
<html lang="en">
<head>
<meta charset="utf-8">
<title>Lanterns of Calm – Non Profit Mental Health Agency</title>
<link href="https://fonts.googleapis.com/css2?family=Abril+Fatface&family=Figtree:wght@400;500;600;700&display=swap" rel="stylesheet">
<style>
:root{
  --navy:#0f1f3d;
  --navy-2:#172a4d;
  --slate:#61779b;
  --gold:#e7a50c;
  --gold-text:#f2b51d;
  --white:#ffffff;
  --ink:#1c2436;
  --muted:#555d6b;
  --line:#2c3d5e;
}
*{box-sizing:border-box;margin:0;padding:0}
html,body{width:1200px;height:4100px;overflow:hidden;background:var(--white)}
body{position:relative;font-family:"Figtree",sans-serif;color:var(--ink)}
.abs{position:absolute}
.serif{font-family:"Abril Fatface",serif;font-weight:400}
.btn{position:absolute;display:flex;align-items:center;justify-content:center;background:var(--gold);color:var(--white);border-radius:30px;font-size:13px;font-weight:700;letter-spacing:.3px;text-transform:uppercase}
.photo{position:absolute}

/* hero */
.hero{left:0;top:0;width:1200px;height:737px;background:linear-gradient(90deg,#1d1a16 0%,#3a3128 45%,#6a5a48 75%,#4a4035 100%)}
.topbar{left:457px;top:0;width:743px;height:32px;background:var(--navy);border-bottom-left-radius:22px;display:flex;align-items:center;color:var(--white);font-size:14px}
.topbar .sq{width:12px;height:12px;border-radius:3px;background:var(--white);margin-left:26px}
.topbar .contact{margin-left:auto;display:flex;gap:26px;padding-right:66px;align-items:center}
.topbar .contact span{display:flex;align-items:center;gap:8px}
.brand{left:67px;top:20px;width:140px;text-align:center;color:var(--gold-text);font-family:"Figtree",sans-serif;font-weight:600;font-size:15px;line-height:1.2;letter-spacing:.5px}
.brand .dot{width:44px;height:44px;border-radius:50%;background:var(--gold-text);margin:0 auto 6px}
.nav{left:457px;top:56px;display:flex;gap:50px;font-size:13px;color:var(--white);text-transform:uppercase;line-height:20px}
.nav .active{color:var(--gold-text)}
.kicker{left:67px;top:262px;color:var(--white);font-size:19px;letter-spacing:2.5px}
.hero-title{left:67px;top:292px;color:var(--white);font-size:48px;line-height:58px}
.gold{color:var(--gold-text)}
.hero-text{left:67px;top:423px;width:450px;color:var(--white);font-size:17px;line-height:27px}

/* mission */
.mission{left:67px;top:649px;width:533px;height:422px;background:var(--slate)}
.mission-title{left:315px;top:700px;width:280px;text-align:center;color:var(--white);font-size:42px;line-height:50px}
.mission-text{left:330px;top:818px;width:250px;text-align:center;color:var(--white);font-size:15px;line-height:24px}
.welcome{left:600px;top:1007px;width:533px;height:397px;background:var(--navy)}
.welcome .small{position:absolute;top:58px;width:100%;text-align:center;color:var(--white);font-size:15px;letter-spacing:.5px}
.welcome h2{position:absolute;top:80px;width:100%;text-align:center;color:var(--white);font-size:40px;font-weight:400;font-family:"Abril Fatface",serif}
.welcome p{position:absolute;top:148px;left:22px;width:489px;text-align:center;color:var(--white);font-size:15px;line-height:24px}

/* therapists */
.eyebrow{width:1200px;left:0;text-align:center;font-size:15px;color:var(--ink)}
.section-title{width:1200px;left:0;text-align:center;font-size:40px;color:var(--ink)}
.card{position:absolute;top:1614px;width:261px;height:323px}
.card .cap{position:absolute;bottom:0;width:100%;height:72px;background:linear-gradient(180deg,rgba(15,31,61,0) 0%,rgba(15,31,61,.7) 100%);text-align:center;color:var(--white)}
.card .name{position:absolute;top:28px;width:100%;font-family:"Abril Fatface",serif;font-size:20px}
.card .role{position:absolute;top:52px;width:100%;font-size:13px}

/* donate */
.donate{left:0;top:2042px;width:1200px;height:511px;background:linear-gradient(90deg,#26324c 0%,#34415c 50%,#263149 100%)}
.donate-title{left:0;top:2170px;width:1200px;text-align:center;color:var(--white);font-size:58px;line-height:66px}
.donate-text{left:0;top:2315px;width:1200px;text-align:center;color:var(--white);font-size:18px}

/* blog */
.post{position:absolute;top:2760px;width:348px}
.post .img{height:215px;position:relative}
.post .date{position:absolute;left:6px;top:6px;width:57px;height:52px;background:var(--white);padding:6px 0 0 12px}
.post .date b{display:block;font-family:"Abril Fatface",serif;font-weight:400;font-size:20px;color:var(--navy);line-height:20px}
.post .date i{font-style:normal;font-size:11px;color:var(--ink)}
.post h3{margin-top:16px;font-family:"Abril Fatface",serif;font-weight:400;font-size:19px;color:var(--navy)}
.post p{margin-top:9px;font-size:15px;line-height:24px;color:var(--muted)}
.post .btn{position:relative;margin-top:20px;width:138px;height:43px}

/* mailing */
.mail{left:67px;top:3236px;width:1066px;height:334px;border-radius:167px;background:linear-gradient(90deg,#7a4a3a 0%,#8f8a88 25%,#3f4a60 45%,#2a354d 60%,#27324a 100%);overflow:hidden}
.mail-title{left:535px;top:3284px;width:540px;text-align:center;color:var(--white);font-size:38px}
.field{position:absolute;height:45px;background:var(--white);border-radius:23px;font-size:12px;color:#444;padding-left:24px;display:flex;align-items:center}

/* footer */
.footer{left:0;top:3675px;width:1200px;height:425px;background:var(--navy)}
.f-brand{left:67px;top:3735px;width:251px;text-align:center}
.f-brand .dot{width:150px;height:150px;border-radius:50%;background:var(--gold-text);margin:0 auto 18px}
.f-brand .word{color:var(--gold-text);font-size:25px;font-weight:600;letter-spacing:1px}
.f-head{font-family:"Abril Fatface",serif;font-size:19px;color:var(--gold-text)}
.f-link{left:481px;color:var(--white);font-size:15px}
.f-item{left:695px;display:flex;gap:10px;color:var(--white);font-size:15px;line-height:22px}
.icon{width:32px;height:32px;border-radius:4px;background:var(--gold);display:flex;align-items:center;justify-content:center;flex:none}
.soc{left:1030px;display:flex;align-items:center;gap:11px;color:var(--white);font-size:13px}
.soc .sq{width:32px;height:32px;border-radius:4px;background:var(--navy-2);display:flex;align-items:center;justify-content:center}
.soc .sq i{width:12px;height:12px;background:var(--white);border-radius:2px}
.rule{left:67px;top:4007px;width:1066px;height:1px;background:var(--line)}
.copy{left:0;top:4032px;width:1200px;text-align:center;color:var(--white);font-size:12px}
</style>
</head>
<body>

<!-- Hero -->
<section class="abs hero" role="img" aria-label="Photo of two women in a support group holding hands and comforting each other"></section>
<div class="abs topbar">
  <span class="sq"></span><span class="sq"></span><span class="sq"></span>
  <div class="contact">
    <span><svg width="14" height="14" viewBox="0 0 24 24"><path fill="#e7a50c" d="M6.6 10.8a15 15 0 0 0 6.6 6.6l2.2-2.2c.3-.3.7-.4 1-.2 1.1.4 2.3.6 3.6.6.6 0 1 .4 1 1V20c0 .6-.4 1-1 1A17 17 0 0 1 3 4c0-.6.4-1 1-1h3.5c.6 0 1 .4 1 1 0 1.3.2 2.5.6 3.6.1.3 0 .7-.2 1z"/></svg>(555) 014-2290</span>
    <span><svg width="16" height="14" viewBox="0 0 24 20"><rect x="1.5" y="1.5" width="21" height="17" rx="2" fill="none" stroke="#e7a50c" stroke-width="2"/><path d="M2 3l10 8 10-8" fill="none" stroke="#e7a50c" stroke-width="2"/></svg>hello@lanternsofcalm.org</span>
  </div>
</div>
<div class="abs brand"><div class="dot"></div>LANTERNS OF CALM</div>
<nav class="abs nav"><span class="active">Home</span><span>About Us</span><span>Therapists</span><span>Blog</span><span>Contact Us</span></nav>
<a class="btn" style="left:996px;top:45px;width:137px;height:43px">Donate Now</a>
<div class="abs kicker">WE ARE A FAITH FRIENDLY</div>
<h1 class="abs hero-title serif">Non Profit Mental<br>Health <span class="gold">Agency</span></h1>
<p class="abs hero-text">Lanterns of Calm crosses barriers to mental health care for Ohioans.</p>
<a class="btn" style="left:67px;top:500px;width:137px;height:43px">Donate Now</a>

<!-- Mission / About -->
<section class="abs mission"></section>
<div class="photo" style="left:84px;top:667px;width:231px;height:388px;background:linear-gradient(180deg,#6b5a4a,#a89a8c 50%,#3f3a3c)" role="img" aria-label="Photo of a counselor leading a group therapy circle"></div>
<h2 class="abs mission-title serif">Our<br>Mission</h2>
<p class="abs mission-text">Lanterns of Calm is a 501(c)(3) nonprofit organization that offers counseling to Ohioans who cannot access mental health care. We envision a community...</p>
<a class="btn" style="left:387px;top:964px;width:137px;height:42px">Read More</a>
<div class="photo" style="left:600px;top:737px;width:533px;height:270px;background:linear-gradient(90deg,#5d5a52,#a9a79a 50%,#6f6a5c)" role="img" aria-label="Photo of a group of adults praying together"></div>
<div class="photo" style="left:67px;top:1071px;width:533px;height:333px;background:linear-gradient(90deg,#8a6a3c,#d9d8d3 45%,#e9eaea 75%,#5a5a5e)" role="img" aria-label="Photo of a support group comforting one member"></div>
<section class="abs welcome">
  <div class="small">WELCOME TO</div>
  <h2>Lanterns of Calm</h2>
  <p>Mental health impacts every element of our daily lives. From the ways that we work to how we relate with our families, mental wellness allows us to be present in the moment and contribute positively to our communities. Unfortunately, many of our neighbors in Ohio face mental health challenges which harm their quality of life....</p>
</section>
<a class="btn" style="left:797px;top:1300px;width:137px;height:43px">Read More</a>

<!-- Therapists -->
<div class="abs eyebrow" style="top:1504px">DOCTORS</div>
<h2 class="abs section-title serif" style="top:1524px">Meet Therapists</h2>
<div class="card" style="left:67px;background:linear-gradient(180deg,#e7b28e,#c99b7c)" role="img" aria-label="Portrait of a smiling therapist with a beard">
  <div class="cap"><div class="name">Aaron Vellmont</div><div class="role">Trauma Specialist</div></div></div>
<div class="card" style="left:336px;background:linear-gradient(180deg,#0f1726,#2c4a78)" role="img" aria-label="Portrait of a therapist in blue scrubs">
  <div class="cap"><div class="name">Silas Dorrane</div><div class="role">Anxiety Specialist</div></div></div>
<div class="card" style="left:603px;background:linear-gradient(180deg,#f2f2f2,#8a5a48)" role="img" aria-label="Portrait of a therapist with long auburn hair">
  <div class="cap"><div class="name">Marina Ostell</div><div class="role">Depression Specialist</div></div></div>
<div class="card" style="left:872px;background:linear-gradient(180deg,#7bb3c4,#dde6ea)" role="img" aria-label="Portrait of a smiling therapist making a heart with his hands">
  <div class="cap"><div class="name">Wilder Dunmore</div><div class="role">Anxiety Specialist</div></div></div>

<!-- Donate -->
<section class="abs donate" role="img" aria-label="Dimmed photo of a group therapy session"></section>
<h2 class="abs donate-title serif"><span class="gold">Donor</span> Support and<br>Community <span class="gold">Partnerships</span></h2>
<p class="abs donate-text">Allow us to meet and serve individuals who could not otherwise access professional care.</p>
<a class="btn" style="left:532px;top:2367px;width:136px;height:43px">Donate Now</a>

<!-- Blog -->
<div class="abs eyebrow" style="top:2652px">ARTICLE POST</div>
<h2 class="abs section-title serif" style="top:2672px">Recent Blog Post</h2>
<article class="post" style="left:67px">
  <div class="img" style="background:linear-gradient(90deg,#8b8a84,#d8cfb8 50%,#6d6c6a)" role="img" aria-label="Photo of a group holding a mental health sketch board"><div class="date"><b>22</b><i>Jun, 24</i></div></div>
  <h3>Excepteur sint occaecat magna</h3>
  <p>Duis aute irure dolor in reprehenderit in voluptate velit esse cillum dolore...</p>
  <a class="btn">Read More</a>
</article>
<article class="post" style="left:426px">
  <div class="img" style="background:linear-gradient(90deg,#6f6a63,#b8b2a6 60%,#d9d3c9)" role="img" aria-label="Photo of a smiling group in a counseling session"><div class="date"><b>22</b><i>Jun, 24</i></div></div>
  <h3>Excepteur sint occaecat magna</h3>
  <p>Duis aute irure dolor in reprehenderit in voluptate velit esse cillum dolore...</p>
  <a class="btn">Read More</a>
</article>
<article class="post" style="left:785px">
  <div class="img" style="background:linear-gradient(90deg,#6b7a6a,#b9c2b3 50%,#7a8a76)" role="img" aria-label="Photo of a support group seated in a circle"><div class="date"><b>22</b><i>Jun, 24</i></div></div>
  <h3>Excepteur sint occaecat magna</h3>
  <p>Duis aute irure dolor in reprehenderit in voluptate velit esse cillum dolore...</p>
  <a class="btn">Read More</a>
</article>

<!-- Mailing list -->
<section class="abs mail" role="img" aria-label="Photo of a counselor comforting a distressed man"></section>
<h2 class="abs mail-title serif">Join Mailing List</h2>
<div class="field" style="left:535px;top:3361px;width:265px">Your Name</div>
<div class="field" style="left:808px;top:3361px;width:265px">Enter Phone:</div>
<div class="field" style="left:535px;top:3417px;width:538px">Your Email:</div>
<a class="btn" style="left:535px;top:3474px;width:138px;height:40px">Send</a>

<!-- Footer -->
<footer class="abs footer"></footer>
<div class="abs f-brand"><div class="dot"></div><div class="word">LANTERNS OF CALM</div></div>
<div class="abs f-head" style="left:481px;top:3722px">Quick Links</div>
<div class="abs f-link" style="top:3774px">Home</div>
<div class="abs f-link" style="top:3810px">About Us</div>
<div class="abs f-link" style="top:3845px">Therapist</div>
<div class="abs f-link" style="top:3881px">Blog</div>
<div class="abs f-link" style="top:3916px">Contact Us</div>

<div class="abs f-head" style="left:695px;top:3722px">Contact Us</div>
<div class="abs f-item" style="top:3780px"><span class="icon"><svg width="14" height="16" viewBox="0 0 24 28"><path fill="#fff" d="M12 0a10 10 0 0 0-10 10c0 7.5 10 18 10 18s10-10.5 10-18A10 10 0 0 0 12 0zm0 14a4 4 0 1 1 0-8 4 4 0 0 1 0 8z"/></svg></span><span>25 Lorem ipsum dolor sit amet<br>Glassglo 25KM SUA</span></div>
<div class="abs f-item" style="top:3853px"><span class="icon"><svg width="14" height="14" viewBox="0 0 24 24"><path fill="#fff" d="M6.6 10.8a15 15 0 0 0 6.6 6.6l2.2-2.2c.3-.3.7-.4 1-.2 1.1.4 2.3.6 3.6.6.6 0 1 .4 1 1V20c0 .6-.4 1-1 1A17 17 0 0 1 3 4c0-.6.4-1 1-1h3.5c.6 0 1 .4 1 1 0 1.3.2 2.5.6 3.6.1.3 0 .7-.2 1z"/></svg></span><span style="padding-top:5px">(555) 014-2290</span></div>
<div class="abs f-item" style="top:3911px"><span class="icon"><svg width="16" height="13" viewBox="0 0 24 20"><rect x="1.5" y="1.5" width="21" height="17" rx="2" fill="none" stroke="#fff" stroke-width="2"/><path d="M2 3l10 8 10-8" fill="none" stroke="#fff" stroke-width="2"/></svg></span><span style="padding-top:5px">hello@lanternsofcalm.org</span></div>

<div class="abs f-head" style="left:1030px;top:3722px">Follow Us</div>
<div class="abs soc" style="top:3780px"><span class="sq"><i></i></span>Facepage</div>
<div class="abs soc" style="top:3825px"><span class="sq"><i></i></span>Picturegram</div>
<div class="abs soc" style="top:3871px"><span class="sq"><i></i></span>Linkwork</div>

<div class="abs rule"></div>
<div class="abs copy">© <span class="gold">LANTERNS OF CALM</span>, 2024. ALL RIGHTS RESERVED.</div>

</body>
</html>
```